CBD Banner Ad for Print and Plimbo

I we would like a modern European chic that we can use in a 1/4 page ad in our local magazine and also use as our banner ad in the Plimbo ad searches. <br/><br/>We are a high end CBD boutique shop that has their own brand as well as a carefully curated selection of the top end CBD products out on the market. The final design should promote the health and well being that we are trying to live ourselves. We DO NOT want the use of marijuana paraphernalia or like substances. Think Yoga Studio meets Morvette inside of a health store. <br/><br/>Use any images you would like...I have attached a sample product render as well as the inside of our store...but take this in the direction you would like.<br/><br/>The winner will have the added bonus of being able to create 10 more ads for us in the next 6 months.

Target Market(s)

Our target market are the middle to upperclass professional workers that want to take CBD but were afraid due to misinformation or stigma

Font styles to use
Sans Serif

Colors
33b8a4
86cfc6
0792cd
3277b5
85acd3

Requirements
Must have
• A good clean modern design.
• Natural. Organic. Crisp. Welcoming.
Nice to have
• Tess Hollow
• CBD for wellness. CBD for life.
• The font we use for the rest of our campaigns is Adam.
Should not have
• Absolutely NO marijuana leaves, paraphernalia, or references. We are working hard to educate people and get rid of the stigma.

```html
<!DOCTYPE html>
<html lang="en">
<head>
<meta charset="utf-8">
<title>Tess Hollow – CBD banner set</title>
<link rel="stylesheet" href="https://fonts.googleapis.com/css2?family=Lato:wght@300;400;700&display=swap">
<style>
  :root {
    --canvas: #ffffff;
    --panel-blue: #88aed5;
    --script-wash: rgba(164, 196, 228, 0.55);
    --script-fade: rgba(164, 196, 228, 0);
    --frame-line: rgba(255, 255, 255, 0.38);
    --logo-ink: #4b5860;
    --logo-paper: #ffffff;
    --logo-rule: #c9cfd3;
    --tagline: #ffffff;
    --leaf-deep: #2d6338;
    --leaf-mid: #3f7a4a;
    --leaf-light: #dfe8e2;
    --skin: #d6a487;
    --shadow: rgba(40, 50, 60, 0.28);
  }
  * { box-sizing: border-box; margin: 0; padding: 0; }
  html, body {
    width: 1200px; height: 900px; overflow: hidden;
    background: var(--canvas);
    font-family: "Lato", Arial, sans-serif;
  }
  .canvas { position: relative; width: 1200px; height: 900px; }

  .banner {
    position: absolute;
    overflow: hidden;
    background: var(--panel-blue);
  }
  .banner--leaderboard { left: 58px; top: 143px; width: 718px; height: 297px; box-shadow: 0 14px 14px -8px var(--shadow); }
  .banner--square { left: 476px; top: 520px; width: 296px; height: 246px; box-shadow: 0 12px 12px -8px var(--shadow); }
  .banner--skyscraper { left: 830px; top: 164px; width: 297px; height: 592px; box-shadow: -6px 8px 12px -6px var(--shadow); }

  .photo {
    position: absolute;
    background:
      radial-gradient(ellipse 30% 55% at 58% 62%, var(--skin) 0%, rgba(214,164,135,0.85) 45%, rgba(214,164,135,0) 80%),
      linear-gradient(120deg, var(--leaf-deep) 0%, var(--leaf-mid) 30%, var(--leaf-light) 55%, #4a8354 80%, var(--leaf-deep) 100%);
  }
  .banner--leaderboard .photo { left: 274px; top: 0; right: 0; bottom: 0; }
  .banner--square .photo { left: 135px; top: 0; right: 0; bottom: 0; }
  .banner--skyscraper .photo {
    left: 0; top: 0; right: 0; height: 251px;
    background:
      radial-gradient(ellipse 40% 75% at 50% 55%, var(--skin) 0%, rgba(214,164,135,0.85) 50%, rgba(214,164,135,0) 85%),
      linear-gradient(100deg, var(--leaf-deep) 0%, var(--leaf-light) 30%, #3a7545 70%, var(--leaf-deep) 100%);
  }

  /* soft wash where the faint script word sits */
  .script-wash {
    position: absolute;
    background: radial-gradient(ellipse 50% 50% at 50% 50%, var(--script-wash) 0%, var(--script-fade) 100%);
  }
  .banner--leaderboard .script-wash { left: 30px; top: 30px; width: 240px; height: 150px; }
  .banner--square .script-wash { left: 14px; top: 16px; width: 130px; height: 90px; }
  .banner--skyscraper .script-wash { left: 30px; top: 330px; width: 290px; height: 165px; }

  .frame {
    position: absolute;
    border: 1px solid var(--frame-line);
    pointer-events: none;
  }
  .banner--leaderboard .frame { left: 19px; top: 16px; width: 680px; height: 265px; }
  .banner--square .frame { left: 15px; top: 15px; width: 265px; height: 216px; }
  .banner--skyscraper .frame { left: 16px; top: 14px; width: 265px; height: 562px; }

  .brand-box {
    position: absolute;
    background: var(--logo-paper);
    box-shadow: 0 1px 3px rgba(0,0,0,0.12);
    display: flex; align-items: center; justify-content: center;
  }
  .brand-box::before {
    content: "";
    position: absolute; inset: 4px;
    border: 1px solid var(--logo-rule);
  }
  .brand-name {
    position: relative;
    color: var(--logo-ink);
    font-weight: 300;
    text-transform: uppercase;
    white-space: nowrap;
  }
  .banner--leaderboard .brand-box { left: 184px; top: 87px; width: 186px; height: 111px; }
  .banner--skyscraper .brand-box { left: 56px; top: 210px; width: 186px; height: 111px; }
  .banner--leaderboard .brand-name,
  .banner--skyscraper .brand-name { font-size: 20px; letter-spacing: 2px; }
  .banner--square .brand-box { left: 35px; top: 91px; width: 108px; height: 65px; }
  .banner--square .brand-name { font-size: 11px; letter-spacing: 1px; }

  .tagline {
    position: absolute;
    color: var(--tagline);
    font-weight: 400;
    text-align: right;
    white-space: nowrap;
  }
  .banner--leaderboard .tagline { right: 455px; top: 220px; font-size: 21px; line-height: 26px; }
  .banner--square .tagline { right: 165px; top: 194px; font-size: 14px; line-height: 17px; }
  .banner--skyscraper .tagline { right: 24px; top: 515px; font-size: 20px; line-height: 24px; }
</style>
</head>
<body>
<main class="canvas">

  <section class="banner banner--leaderboard">
    <div class="photo" role="img" aria-label="Photo of a woman with hands framing her face in front of large green tropical leaves"></div>
    <div class="script-wash" role="img" aria-label="Faint script lettering reading Natural"></div>
    <div class="frame"></div>
    <div class="brand-box"><span class="brand-name">Tess Hollow</span></div>
    <p class="tagline">CBD for wellness.<br>CBD for life.</p>
  </section>

  <section class="banner banner--square">
    <div class="photo" role="img" aria-label="Photo of a smiling woman looking over her shoulder in front of green tropical leaves"></div>
    <div class="script-wash" role="img" aria-label="Faint script lettering reading Natural"></div>
    <div class="frame"></div>
    <div class="brand-box"><span class="brand-name">Tess Hollow</span></div>
    <p class="tagline">CBD for wellness.<br>CBD for life.</p>
  </section>

  <section class="banner banner--skyscraper">
    <div class="photo" role="img" aria-label="Photo of a woman with eyes closed in front of green tropical leaves"></div>
    <div class="script-wash" role="img" aria-label="Faint script lettering reading Natural"></div>
    <div class="frame"></div>
    <div class="brand-box"><span class="brand-name">Tess Hollow</span></div>
    <p class="tagline">CBD for wellness.<br>CBD for life.</p>
  </section>

</main>
</body>
</html>
```